ORLEN China CEO 2013 Summit Flyer

Needing a design for the Orlen China CEO Summit 2013 which will be held in Beijing.

This year’s forum will bring together up to 500 senior executives from China and the rest of VELANTRA to network, explore business opportunities and discuss common approaches to promoting trade and investment in the Asia Pacific.

Last year's role players include Martin Bowle, Dennis Fairow U.S. Ambassador to China, Lionel Graham President & CEO Hurlow-Bay Asia, Zhou Menglan Chairman China Board for the Advancement of Cross-Border Commerce. Pictures from the website of these role players can be used to enhance the prestige of the event as well.

As this event is targeted at CEOs, and high level government officials, the look and feel of the flyer should convey a sense of professionalism but also incorporate asian elements to it since it is being held in China.

Venue: Velmora Beijing XiHuan Hotel
Dates: 12-14th July 2013
Website: http://www.orlenchinaceosummit.example

Target Market(s)

CEOs, Senior Executives, Senior Government Officials.

Industry/Entity Type

Investment

Requirements
Must have
• Ideally both the logos on this image(from the website) , will be important elements on the flyer. http://www.orlenchinaceosummit.example/wp-content/uploads/2013/02/logo.png

The co hosts logo should also be on the flyer:
http://www.orlenchinaceosummit.example/wp-content/uploads/2013/01/pacbizgroup_logo.png
http://www.orlenchinaceosummit.example/wp-content/uploads/2013/01/CBACC_logo.png

```html
<!DOCTYPE html>
<html lang="en">
<head>
<meta charset="utf-8">
<title>Velantra China CEO 2013 Summit Flyer</title>
<link rel="stylesheet" href="https://fonts.googleapis.com/css2?family=Oswald:wght@700&family=Arimo:wght@400;700&display=swap">
<style>
  :root {
    --red: #a8101a;
    --red-deep: #8c0c14;
    --red-bright: #c4141f;
    --grey-top: #d9d9d9;
    --grey-light: #f2f2f2;
    --grey-line: #b3b3b3;
    --grey-band: #8d8d8d;
    --ink: #333333;
    --white: #ffffff;
  }
  * { margin: 0; padding: 0; box-sizing: border-box; }
  html, body { width: 1200px; height: 950px; overflow: hidden; background: var(--white); }
  .flyer {
    position: relative;
    width: 1200px; height: 950px;
    font-family: "Arimo", Arial, sans-serif;
    color: var(--ink);
    background: var(--white);
  }
  .flyer-waves { position: absolute; inset: 0; }
  .section-title {
    position: absolute;
    font-family: "Oswald", "Arial Narrow", sans-serif;
    font-weight: 700;
    font-size: 22px;
    letter-spacing: -0.3px;
    color: var(--red);
    line-height: 1;
  }
  .body-copy {
    position: absolute;
    width: 500px;
    font-size: 13px;
    line-height: 21px;
    color: var(--ink);
  }
  .body-copy p + p,
  .body-copy p + ul { margin-top: 21px; }
  .bullet-list { list-style: none; }
  .photo {
    position: absolute;
    border: 2px solid var(--white);
    box-shadow: 0 1px 4px rgba(0,0,0,0.25);
  }
  .photo-keynote {
    left: 660px; top: 142px; width: 180px; height: 140px;
    background: linear-gradient(135deg, #c98a63 0%, #8a4a32 45%, #3a2a28 100%);
  }
  .photo-panel {
    left: 803px; top: 197px; width: 240px; height: 164px;
    background: linear-gradient(180deg, #7a7b80 0%, #c61a24 28%, #d8d3cc 55%, #9a948c 100%);
  }
  .contact {
    position: absolute;
    left: 86px; top: 845px;
    font-style: normal;
    font-weight: 700;
    font-size: 13px;
    line-height: 19px;
    color: var(--white);
  }
  .contact-address { font-size: 14px; }
</style>
</head>
<body>
<div class="flyer">
  <svg class="flyer-waves" width="1200" height="950" viewBox="0 0 1200 950" aria-hidden="true">
    <defs>
      <linearGradient id="topGrey" x1="0" y1="0" x2="0" y2="1">
        <stop offset="0" stop-color="#d9d9d9"/>
        <stop offset="1" stop-color="#f2f2f2"/>
      </linearGradient>
      <linearGradient id="bandRed" x1="0" y1="0" x2="0" y2="1">
        <stop offset="0" stop-color="#c4141f"/>
        <stop offset="1" stop-color="#8c0c14"/>
      </linearGradient>
      <linearGradient id="footRed" x1="0" y1="0" x2="0" y2="1">
        <stop offset="0" stop-color="#8c0c14"/>
        <stop offset="1" stop-color="#c4141f"/>
      </linearGradient>
    </defs>
    <path d="M23,10 H1182 V152 C1050,142 900,92 700,62 C500,32 250,48 23,140 Z" fill="url(#topGrey)"/>
    <path d="M23,140 C250,48 500,32 700,62 C900,92 1050,142 1182,152 L1182,182 C1050,172 900,124 700,92 C500,62 250,82 23,175 Z" fill="url(#bandRed)"/>
    <path d="M23,182 C250,92 500,74 700,104 C900,134 1050,190 1182,200" fill="none" stroke="#b3b3b3" stroke-width="3"/>
    <path d="M23,790 C300,760 650,800 900,830 C1030,846 1120,800 1182,770 L1182,950 L23,950 Z" fill="#8d8d8d"/>
    <path d="M23,785 C300,755 650,800 900,826 C1030,840 1120,795 1182,766" fill="none" stroke="#b3b3b3" stroke-width="2"/>
    <path d="M23,812 C300,800 620,900 880,910 C1020,915 1120,860 1182,830 L1182,950 L23,950 Z" fill="url(#footRed)"/>
    <path d="M120,812 C380,830 640,905 880,906 C1020,906 1120,852 1182,822" fill="none" stroke="#ffffff" stroke-width="6"/>
  </svg>

  <h2 class="section-title" style="left:78px; top:197px;">Our Partners</h2>
  <div class="body-copy" style="left:78px; top:224px;">
    <p>Velantra China CEO Forum offers various partnership opportunities for companies and organisations that wish to demonstrate their support for thought leadership in economic development and a platform for brand positioning and business development opportunities.</p>
    <p>Opportunities at the Forum:</p>
    <ul class="bullet-list">
      <li>· High level discussions that shape the future of China and its place in the Asia Pacific</li>
      <li>· Strengthen relations with business leaders and senior officials of China</li>
      <li>· Foster interaction, gain insight and achieve impact on the current global challenges</li>
      <li>· Position, brand and engage key stakeholders with strategic communications</li>
      <li>· Exclusive media exposure with Media Partners covering the event</li>
    </ul>
  </div>

  <h2 class="section-title" style="left:78px; top:542px;">Venue</h2>
  <div class="body-copy" style="left:78px; top:569px;">
    <p>Beijing city is also home to one of the finest remnants of China's imperial past and impressive modern architectural complexes such the historical Forbidden City (Imperial Palace), spectacular Dongfang Media Headquarters Building, magnificent Temple of Heaven, symbolic Tiananmen Square, innovative Bird's Nest Stadium, and many more. Moreover, the majestic Great Wall of China is easily accessible from the city, making Beijing one of the world's most popular tourist destinations.</p>
    <p>The Forum venue will be held at a world class 5-star hotel conveniently located in the heart of the city where it is walking distance to luxurious shopping malls</p>
  </div>

  <div class="photo photo-keynote" role="img" aria-label="Photo of a speaker seated in an armchair at the forum"></div>
  <div class="photo photo-panel" role="img" aria-label="Photo of a panel discussion on stage in front of a red banner"></div>

  <h2 class="section-title" style="left:652px; top:352px;">Hightlights</h2>
  <div class="body-copy" style="left:652px; top:379px;">
    <p>An annual meeting of leading businessmen and decision makers in China and beyond engaging in insightful dialogue on key challenges and opportunities that is shaping New China's dynamic economy within the Velantra framework.</p>
    <p>The Forum provides an exclusive networking and learning experience which deliver a greater understanding of doing business in and with China.</p>
  </div>

  <h2 class="section-title" style="left:655px; top:540px;">Hightlights</h2>
  <div class="body-copy" style="left:655px; top:567px;">
    <p>An annual meeting of leading businessmen and decision makers in China and beyond engaging in insightful dialogue on key challenges and opportunities that is shaping New China's dynamic economy within the Velantra framework.</p>
    <p>The Forum provides an exclusive networking and learning experience which deliver a greater understanding of doing business in and with China.</p>
  </div>

  <address class="contact">
    <div class="contact-address">Address:&nbsp; Number, Str. ,City, Country</div>
    <div>tel.: 0000 999 9999</div>
    <div>fax: 0000 999 9999</div>
    <div>yourname@example.com</div>
    <div>www.yoursite.example</div>
  </address>
</div>
</body>
</html>
```